Business Card Design with new logo

Warren Peltzman 4175
E 118th Rd Casey, IL 62420
Cell: 217-555-0187
peltzmanrebuilds@mailhollow.com

Classic Car Restoration Services Buy Sell Trade Consign

Contact Information for Business Card

Warren Peltzman 9698
Cell: 217-555-0187

```html
<!DOCTYPE html>
<html lang="en">
<head>
<meta charset="utf-8">
<title>Peltzman Rebuilds LLC — Business Cards</title>
<link rel="stylesheet" href="https://fonts.googleapis.com/css2?family=Roboto:wght@400;500&display=swap">
<style>
  :root {
    --backdrop: #3a3a3a;
    --paper: #ffffff;
    --red: #c8101a;
    --red-band: #b40d16;
    --red-deep: #9e0a12;
    --navy: #0a121b;
    --ink: #ffffff;
    --brand-red: #d8231e;
    --card-w: 600px;
    --card-h: 343px;
  }
  * { box-sizing: border-box; margin: 0; padding: 0; }
  html, body { width: 1200px; height: 906px; overflow: hidden; }
  body {
    background: var(--backdrop);
    font-family: "Roboto", Arial, sans-serif;
    display: flex;
    flex-direction: column;
    align-items: center;
    justify-content: center;
    gap: 48px;
  }
  .card {
    width: var(--card-w);
    height: var(--card-h);
    position: relative;
    overflow: hidden;
    box-shadow: 0 12px 30px rgba(0,0,0,.45);
  }

  /* Front */
  .card--front { display: flex; }
  .front__brand {
    width: 42%;
    background: var(--paper);
    display: flex;
    align-items: center;
    justify-content: center;
    padding: 0 12px;
  }
  .brand-name {
    color: var(--brand-red);
    font-weight: 500;
    text-align: center;
    line-height: 1.15;
    letter-spacing: .04em;
  }
  .front__brand .brand-name { font-size: 21px; }
  .brand-name small {
    display: block;
    font-size: .55em;
    letter-spacing: .35em;
    margin-top: 6px;
  }
  .front__details {
    flex: 1;
    background: var(--red);
    color: var(--ink);
    position: relative;
  }
  .holder-name {
    position: absolute;
    top: 42px;
    left: 36px;
    font-size: 24px;
    font-weight: 400;
    white-space: nowrap;
  }
  .contact-list {
    list-style: none;
    position: absolute;
    left: 16px;
    right: 0;
    bottom: 40px;
  }
  .contact-item {
    display: flex;
    align-items: center;
    height: 34px;
    background: var(--red-band);
    margin-top: 4px;
    font-size: 14px;
    white-space: nowrap;
  }
  .contact-icon {
    width: 34px;
    height: 34px;
    background: var(--red-deep);
    display: flex;
    align-items: center;
    justify-content: center;
    margin-right: 14px;
    flex-shrink: 0;
  }
  .contact-icon svg { width: 16px; height: 16px; fill: var(--navy); }

  /* Back */
  .card--back {
    background: var(--navy);
    display: flex;
    flex-direction: column;
    align-items: center;
    justify-content: center;
  }
  .card--back .brand-name { font-size: 44px; }
  .back__rule {
    width: 460px;
    height: 1px;
    background: var(--brand-red);
    margin: 30px 0 14px;
    opacity: .8;
  }
  .tagline {
    color: var(--brand-red);
    font-size: 17px;
    white-space: nowrap;
  }
</style>
</head>
<body>

  <section class="card card--front" aria-label="Business card front">
    <div class="front__brand">
      <p class="brand-name">PELTZMAN REBUILDS<small>LLC</small></p>
    </div>
    <div class="front__details">
      <h1 class="holder-name">Warren Peltzman 4175</h1>
      <ul class="contact-list">
        <li class="contact-item">
          <span class="contact-icon">
            <svg viewBox="0 0 24 24" aria-hidden="true"><path d="M12 2a7 7 0 0 0-7 7c0 5 7 13 7 13s7-8 7-13a7 7 0 0 0-7-7zm0 9.5A2.5 2.5 0 1 1 12 6.5a2.5 2.5 0 0 1 0 5z"/></svg>
          </span>
          E 118th Rd Alder Springs, IL 62099
        </li>
        <li class="contact-item">
          <span class="contact-icon">
            <svg viewBox="0 0 24 24" aria-hidden="true"><path d="M6.6 10.8a15 15 0 0 0 6.6 6.6l2.2-2.2c.3-.3.7-.4 1-.2 1.1.4 2.3.6 3.6.6.6 0 1 .4 1 1V20c0 .6-.4 1-1 1A17 17 0 0 1 3 4c0-.6.4-1 1-1h3.5c.6 0 1 .4 1 1 0 1.3.2 2.5.6 3.6.1.3 0 .7-.2 1z"/></svg>
          </span>
          217-555-0187
        </li>
        <li class="contact-item">
          <span class="contact-icon">
            <svg viewBox="0 0 24 24" aria-hidden="true"><path d="M2 5h20v14H2zm2 2v.5l8 5 8-5V7l-8 5z"/></svg>
          </span>
          peltzmanrebuilds@mailhollow.com
        </li>
      </ul>
    </div>
  </section>

  <section class="card card--back" aria-label="Business card back">
    <p class="brand-name">PELTZMAN REBUILDS<small>LLC</small></p>
    <div class="back__rule"></div>
    <p class="tagline">Classic Car Restoration Services Buy Sell Trade Consign</p>
  </section>

</body>
</html>
```